Dental Business Card

I need Dental oriented business cards.
On the front side -
- on the first line, my name:
Dr Marlo Vintner
- on the second line (just underneath):
Doctor of Dental Medicine
- on the third line, or underneath that or in a corner, I would like the address and phone number:
5182 Ch. Birchfield
Montreal QC H2T 4B9
514-629-5074
- other than that i would maybe like a logo of a tooth, but i want it to be subtle and very basic!
- I would like the card to be preferably black or dark grey-ish with the writing in white
On the other side -
- 2-3 lines with the possibility to write the next appointment the box with the lines should be white, with the rest of the card being black

```html
<!DOCTYPE html>
<html lang="en">
<head>
<meta charset="utf-8">
<title>Dental Business Card – Dr Marlo Vintner</title>
<link rel="stylesheet" href="https://fonts.googleapis.com/css2?family=Jost:wght@400;500;600&family=Poppins:wght@400&display=swap">
<style>
  :root {
    --backdrop: #e4e4e4;
    --card: #000000;
    --ink: #ffffff;
    --shadow: rgba(0, 0, 0, 0.25);
  }
  * { margin: 0; padding: 0; box-sizing: border-box; }
  html, body {
    width: 1200px;
    height: 1200px;
    overflow: hidden;
    background: var(--backdrop);
  }
  .canvas {
    position: relative;
    width: 1200px;
    height: 1200px;
  }
  .card {
    position: absolute;
    left: 212px;
    width: 777px;
    height: 442px;
    background: var(--card);
    color: var(--ink);
    box-shadow: 0 6px 18px var(--shadow);
  }
  .card--front { top: 100px; }
  .card--back { top: 652px; }

  .text { position: absolute; white-space: nowrap; transform: translateY(-50%); }

  /* Front */
  .mark {
    position: absolute;
    left: 158px;
    top: 153px;
    width: 70px;
    height: 70px;
    border: 3px solid var(--ink);
    border-radius: 50%;
  }
  .practice-name {
    left: 193px;
    top: 263px;
    transform: translate(-50%, -50%);
    font-family: "Jost", sans-serif;
    font-weight: 500;
    font-size: 19px;
    letter-spacing: 0.13em;
  }
  .divider {
    position: absolute;
    left: 357px;
    top: 132px;
    width: 1.5px;
    height: 179px;
    background: var(--ink);
  }
  .doctor-name {
    right: 71px;
    top: 98px;
    font-family: "Jost", sans-serif;
    font-weight: 600;
    font-size: 27px;
    letter-spacing: 0.06em;
    text-transform: uppercase;
  }
  .doctor-title {
    right: 72px;
    top: 138px;
    font-family: "Jost", sans-serif;
    font-weight: 400;
    font-size: 17px;
    letter-spacing: 0.12em;
  }
  .contact {
    left: 471px;
    font-family: "Poppins", sans-serif;
    font-weight: 400;
    font-size: 16px;
    letter-spacing: 0.14em;
  }
  .contact--street { top: 243px; }
  .contact--city { top: 277px; }
  .contact--phone { top: 327px; font-size: 17px; }

  /* Back */
  .appointment-row {
    position: absolute;
    left: 177px;
    width: 408px;
    height: 36px;
  }
  .appointment-row--date { top: 143px; }
  .appointment-row--time { top: 207px; }
  .appointment-row--note { top: 270px; }
  .appointment-icon {
    position: absolute;
    left: 0;
    top: 0;
    width: 38px;
    height: 38px;
  }
  .appointment-line {
    position: absolute;
    left: 51px;
    right: 0;
    top: 19px;
    height: 1.5px;
    background: var(--ink);
  }
</style>
</head>
<body>
<main class="canvas">

  <section class="card card--front" aria-label="Business card front">
    <span class="mark" aria-hidden="true"></span>
    <p class="text practice-name">DENTAL MEDICINE</p>
    <span class="divider" aria-hidden="true"></span>
    <h1 class="text doctor-name">Dr Marlo Vintner</h1>
    <p class="text doctor-title">Doctor of Dental Medicine</p>
    <p class="text contact contact--street">5182 Ch. Birchfield</p>
    <p class="text contact contact--city">Montreal QC H2T 4B9</p>
    <p class="text contact contact--phone">514-629-5074</p>
  </section>

  <section class="card card--back" aria-label="Business card back, next appointment">
    <div class="appointment-row appointment-row--date">
      <svg class="appointment-icon" viewBox="0 0 38 38" aria-label="Date">
        <rect x="3" y="6" width="32" height="29" fill="#fff"/>
        <rect x="9" y="2" width="4" height="8" rx="2" fill="#fff" stroke="#000" stroke-width="1.5"/>
        <rect x="25" y="2" width="4" height="8" rx="2" fill="#fff" stroke="#000" stroke-width="1.5"/>
        <rect x="5.5" y="14" width="27" height="18.5" fill="#000"/>
        <g fill="#fff">
          <rect x="8" y="16" width="3.5" height="3"/><rect x="13" y="16" width="3.5" height="3"/><rect x="18" y="16" width="3.5" height="3"/><rect x="23" y="16" width="3.5" height="3"/><rect x="28" y="16" width="2.5" height="3"/>
          <rect x="8" y="21" width="3.5" height="3"/><rect x="13" y="21" width="3.5" height="3"/><rect x="18" y="21" width="3.5" height="3"/><rect x="23" y="21" width="3.5" height="3"/><rect x="28" y="21" width="2.5" height="3"/>
          <rect x="8" y="26" width="3.5" height="3"/><rect x="13" y="26" width="3.5" height="3"/><rect x="18" y="26" width="3.5" height="3"/><rect x="23" y="26" width="3.5" height="3"/><rect x="28" y="26" width="2.5" height="3"/>
        </g>
      </svg>
      <span class="appointment-line"></span>
    </div>
    <div class="appointment-row appointment-row--time">
      <svg class="appointment-icon" viewBox="0 0 38 38" aria-label="Time">
        <circle cx="19" cy="19" r="16" fill="none" stroke="#fff" stroke-width="3"/>
        <path d="M19 9 V20 H27" fill="none" stroke="#fff" stroke-width="3"/>
      </svg>
      <span class="appointment-line"></span>
    </div>
    <div class="appointment-row appointment-row--note">
      <svg class="appointment-icon" viewBox="0 0 38 38" aria-label="Notes">
        <rect x="2" y="1" width="34" height="35" fill="#fff"/>
        <g fill="#000">
          <rect x="7" y="8" width="24" height="3"/>
          <rect x="7" y="14" width="24" height="3"/>
          <rect x="7" y="20" width="24" height="3"/>
          <rect x="7" y="26" width="15" height="3"/>
        </g>
      </svg>
      <span class="appointment-line"></span>
    </div>
  </section>

</main>
</body>
</html>
```